brisknest

i want to ues this logo and the same colors used on the business card

cleaning & service

Industry/Entity Type

Business

Contact Information for Business Card

Font styles to use
Serif
Sans Serif
Decorative
Script

Colors
add136
0692cd
000000
5c5c5c
fbfbfb

Requirements
Must have
• cleaning things

```html
<!DOCTYPE html>
<html lang="en">
<head>
<meta charset="utf-8">
<title>Brisknest business card</title>
<link rel="stylesheet" href="https://fonts.googleapis.com/css2?family=Roboto:wght@400;500;700&display=swap">
<style>
  :root {
    --green: #add136;
    --blue: #0692cd;
    --navy: #1f5fae;
    --white: #fbfbfb;
    --paper: #f4f4f4;
    --grey: #5c5c5c;
    --stage: #e6e4df;
  }
  * { box-sizing: border-box; margin: 0; padding: 0; }
  html, body { width: 1200px; height: 911px; overflow: hidden; }
  body {
    background: var(--stage);
    font-family: "Roboto", Arial, sans-serif;
    position: relative;
  }
  .card {
    position: absolute;
    top: 150px;
    width: 370px;
    height: 610px;
    border-radius: 24px;
    overflow: hidden;
    box-shadow: 0 10px 30px rgba(0,0,0,.18);
  }
  .card--front { left: 180px; background: var(--green); }
  .card--back { left: 650px; background: var(--paper); }

  .front__brand {
    position: absolute;
    top: 150px; left: 0; right: 0;
    text-align: center;
    color: var(--white);
    font-weight: 700;
    font-size: 40px;
    letter-spacing: 1px;
  }
  .front__contact {
    position: absolute;
    left: 34px; top: 370px;
    display: flex;
  }
  .contact__icons {
    display: flex; flex-direction: column;
    gap: 26px; padding-top: 2px; width: 36px;
  }
  .contact__icons svg { width: 18px; height: 18px; fill: var(--navy); }
  .contact__rule { width: 1.5px; background: var(--white); margin: 0 20px 0 10px; height: 150px; }
  .contact__details { color: var(--white); font-size: 16px; line-height: 1; }
  .contact__name { color: var(--navy); font-weight: 700; font-size: 21px; text-transform: uppercase; }
  .contact__role { font-size: 13px; margin: 4px 0 20px; }
  .contact__line { margin-bottom: 18px; }

  .back__brand {
    position: absolute;
    top: 270px; left: 0; right: 0;
    display: flex; align-items: center; justify-content: center; gap: 10px;
    color: var(--navy);
    font-weight: 700;
    font-size: 36px;
  }
  .back__dot { width: 14px; height: 14px; border-radius: 50%; background: var(--green); }
  .back__band {
    position: absolute;
    left: 0; right: 0; bottom: 70px;
    height: 44px;
    background: var(--blue);
    color: var(--white);
    font-size: 15px;
    letter-spacing: 3px;
    display: flex; align-items: center; justify-content: center;
  }
</style>
</head>
<body>
  <section class="card card--front" aria-label="Business card front">
    <div class="front__brand">BRISKNEST</div>
    <div class="front__contact">
      <div class="contact__icons">
        <svg viewBox="0 0 24 24" aria-hidden="true"><circle cx="12" cy="7" r="5"/><path d="M2 23c0-6 4.5-9 10-9s10 3 10 9z"/></svg>
        <svg viewBox="0 0 24 24" aria-hidden="true"><path d="M6.6 10.8a15 15 0 0 0 6.6 6.6l2.2-2.2c.3-.3.7-.4 1-.2 1.1.4 2.3.6 3.6.6.6 0 1 .4 1 1V20c0 .6-.4 1-1 1A17 17 0 0 1 3 4c0-.6.4-1 1-1h3.5c.6 0 1 .4 1 1 0 1.3.2 2.5.6 3.6.1.3 0 .7-.2 1z"/></svg>
        <svg viewBox="0 0 24 24" aria-hidden="true"><path d="M2 5h20v14H2z"/><path d="M2 5l10 8 10-8" fill="none" stroke="#add136" stroke-width="2"/></svg>
        <svg viewBox="0 0 24 24" aria-hidden="true"><circle cx="12" cy="12" r="10"/><path d="M2 12h20M12 2c3 3 3 17 0 20M12 2c-3 3-3 17 0 20" fill="none" stroke="#add136" stroke-width="1.5"/></svg>
      </div>
      <div class="contact__rule"></div>
      <div class="contact__details">
        <div class="contact__name">Dana Reyes</div>
        <div class="contact__role">Owner</div>
        <div class="contact__line">555 214 7390</div>
        <div class="contact__line">dana@brisknest.com</div>
        <div class="contact__line">www.brisknest.com</div>
      </div>
    </div>
  </section>

  <section class="card card--back" aria-label="Business card back">
    <div class="back__brand"><span class="back__dot"></span>Brisknest</div>
    <div class="back__band">WWW.BRISKNEST.COM</div>
  </section>
</body>
</html>
```